Corlow Baptist Church signage beginning in parking lot and carrying through facility.

We want to design a theme/scheme for our signage. Parking lot banners that go on the light poles, banners in the foyer that promote classes being offered, a display about current missional projects- I want them to all have a common look. We have a blue and grey decor that it would need to fit with. The website is Corlow.org I have attached our logo that we use and like and would incorporate. We have six classes that we want to deisgn banners for. We want the banners simple with an icon representing each class- it is a 6 step process so each step would have a banner and icon that represents that step.

The included Word Doc has the description of the classes we want the banners to promote and then file with the banners were some that were presented but not the style I am after. I want simple and informative.
Updates

Project Deadline Extended
Reason: I have not had time to work with the designers contributing so I wanted to extend for five days. Thank you all for your amazing contributions.

Target Market(s)

People that come into our church and parking lot each week.

Industry/Entity Type

Church

Font styles to use
Serif

Colors
0255a3
3b7bb7
85acd3
eaf1f7
fbee3d
fbed22

Requirements
Must have
• Visually inviting, consistent look. A style that can be added to and expanded to include all of our print and signage. We are looking to have banners added to our light poles in our parking lots and want to have something like "welcome home" on those banners. Then we want to have a similar theme carried into our foyer to incorporate into the banners that we use to promote classes etc. and keep our members and visited engaged. We are also building a display of our current mission projects and opportunities and we want to have a consistent look for that as well.
• The idea of using simple Icons to represent the different classes on the banners is appealing to me. A simple background, simple font, simple borders, few colors, with a prominent Icon as the central focus.
Nice to have
• Icon type logos for each of the six banners that represent the six steps in our class series.

```html
<!DOCTYPE html>
<html lang="en">
<head>
<meta charset="utf-8">
<title>Corlow Baptist Church – Step One Banner</title>
<link rel="stylesheet" href="https://fonts.googleapis.com/css2?family=Roboto+Slab:wght@600;700;800&family=Bodoni+Moda:wght@400&display=swap">
<style>
  :root {
    --orange: #f4832f;
    --navy: #1c1f4a;
    --yellow: #f3d21c;
    --yellow-light: #f6e38a;
    --white: #ffffff;
    --ink: #222222;
  }
  * { margin: 0; padding: 0; box-sizing: border-box; }
  html, body { width: 900px; height: 1200px; overflow: hidden; }
  body { background: var(--orange); position: relative; font-family: "Roboto Slab", serif; }

  .banner-panel {
    position: absolute; left: 26px; top: 81px; width: 848px; height: 1093px;
    background: var(--white);
  }
  .panel-frame {
    position: absolute; left: 0; top: 0; width: 848px; height: 1093px;
  }

  .step-header {
    position: absolute; left: 105px; top: 26px; width: 690px; height: 107px;
  }
  .step-title {
    position: absolute; left: 0; top: 0; width: 100%; height: 100%;
    display: flex; align-items: center; justify-content: center;
    font-weight: 800; font-size: 60px; font-variant: small-caps; letter-spacing: 1px;
    color: var(--yellow);
  }
  .step-title .step-number { color: var(--orange); margin-right: 20px; }
  .step-title .step-word { background: linear-gradient(90deg, var(--yellow), var(--yellow-light)); -webkit-background-clip: text; background-clip: text; color: transparent; }

  .class-name {
    position: absolute; left: 0; width: 900px; top: 230px; text-align: center;
    font-weight: 700; font-size: 38px; color: var(--ink);
  }
  .class-name .accent { color: var(--orange); }
  .class-code {
    position: absolute; left: 0; width: 900px; top: 297px; text-align: center;
    font-weight: 700; font-size: 31px; color: var(--navy);
  }
  .class-code .num { color: var(--yellow); }

  .icon-row { position: absolute; left: 0; top: 470px; width: 900px; height: 105px; }
  .leaves-art {
    position: absolute; left: 317px; top: 21px; width: 68px; height: 54px;
    background: radial-gradient(circle at 40% 50%, var(--yellow) 55%, rgba(243,210,28,0) 72%);
  }
  .power-icon { position: absolute; left: 386px; top: 0; }
  .dove-art {
    position: absolute; left: 497px; top: 0; width: 86px; height: 103px;
    background: radial-gradient(ellipse at 50% 50%, var(--yellow) 45%, var(--orange) 60%, rgba(244,131,47,0) 72%);
  }

  .scripture-ref {
    position: absolute; left: 0; width: 900px; top: 623px; text-align: center;
    font-weight: 700; font-size: 38px; color: var(--orange);
  }
  .scripture-ref .chapter { color: var(--navy); }
  .scripture-ref sup { font-size: 18px; color: var(--navy); vertical-align: 18px; margin-left: 4px; }
  .scripture-text {
    position: absolute; left: 120px; width: 660px; top: 695px; text-align: center;
    font-family: "Bodoni Moda", serif; font-size: 28px; line-height: 41.5px; color: var(--ink);
  }
  .scripture-text sup { font-family: "Roboto Slab", serif; font-weight: 700; font-size: 17px; color: var(--orange); vertical-align: 12px; }

  .church-mark {
    position: absolute; left: 0; width: 900px; top: 1080px;
    display: flex; align-items: center; justify-content: center; gap: 12px;
  }
  .church-mark .dot { width: 20px; height: 20px; border-radius: 50%; background: var(--yellow); }
  .church-mark .name { font-weight: 700; font-size: 40px; color: var(--navy); }
</style>
</head>
<body>
  <div class="banner-panel">
    <svg class="panel-frame" width="848" height="1093" viewBox="0 0 848 1093" aria-hidden="true">
      <rect x="6" y="6" width="836" height="1081" fill="none" stroke="var(--navy)" stroke-width="2"/>
      <rect x="12" y="12" width="824" height="1069" fill="none" stroke="var(--navy)" stroke-width="1"/>
    </svg>
  </div>

  <div class="step-header">
    <svg width="690" height="107" viewBox="0 0 690 107" aria-hidden="true">
      <polygon points="20,0 670,0 690,20 690,87 670,107 20,107 0,87 0,20" fill="var(--navy)"/>
    </svg>
    <h1 class="step-title"><span class="step-number">1.</span><span class="step-word">Step One</span></h1>
  </div>

  <h2 class="class-name"><span class="accent">Starting Point</span> (membership)</h2>
  <p class="class-code">Corlow <span class="num">101</span></p>

  <div class="icon-row">
    <div class="leaves-art" role="img" aria-label="Cluster of yellow and orange leaves"></div>
    <svg class="power-icon" width="106" height="105" viewBox="0 0 106 105" aria-label="Power symbol icon" role="img">
      <circle cx="53" cy="53" r="48" fill="none" stroke="var(--navy)" stroke-width="5"/>
      <path d="M38 33 A26 26 0 1 0 68 33" fill="none" stroke="var(--navy)" stroke-width="10" stroke-linecap="round"/>
      <line x1="53" y1="22" x2="53" y2="46" stroke="var(--orange)" stroke-width="5" stroke-linecap="round"/>
    </svg>
    <div class="dove-art" role="img" aria-label="Yellow dove in flight with orange flame wings"></div>
  </div>

  <h3 class="scripture-ref">Hebrews <span class="chapter">10:</span>24-25<sup>24</sup></h3>
  <p class="scripture-text">and let us consider how to stimulate one another to love and good deeds, <sup>25</sup> not forsaking our own assembling together, as is the habit of some, but encouraging one another; and all the more as you see the day drawing near.</p>

  <div class="church-mark">
    <span class="dot"></span>
    <span class="name">Corlow</span>
  </div>
</body>
</html>
```